Website for Excavator and Earthworks Company

We require a modern, sleek and practical website for our newly created earthworks/excavator business in Perth, Western Australia called Gullwind Stonecut Earthworks.

The website should have a modern, cutting edge feel but only needs to be relatively simplistic in it's layout and eventual functionality.

Some pages it should have would be Home, About, Projects and Contact Us.

Number of Pages Required

1 page

```html
<!DOCTYPE html>
<html lang="en">
<head>
<meta charset="utf-8">
<title>Gullwind Stonecut Earthworks</title>
<link href="https://fonts.googleapis.com/css2?family=Lexend:wght@400;500;600&family=Nunito+Sans:wght@400;600;700;800&display=swap" rel="stylesheet">
<style>
:root{
  --lime:#c2d40a;
  --lime-dark:#a9b908;
  --ink:#0d0d0d;
  --charcoal:#161412;
  --text:#555;
  --white:#fff;
  --light:#f4f4f2;
}
*{box-sizing:border-box;margin:0;padding:0}
html,body{width:1200px;height:4326px;overflow:hidden}
body{position:relative;font-family:"Nunito Sans",sans-serif;color:var(--ink);background:var(--white)}
.abs{position:absolute}
.heading{font-family:"Lexend",sans-serif;font-weight:500;text-transform:uppercase;letter-spacing:1px}
.rule{width:66px;height:3px;background:var(--lime)}
.brand{display:flex;align-items:center;gap:12px;font-family:"Nunito Sans",sans-serif;font-weight:800;font-size:20px;letter-spacing:1px;text-transform:uppercase;line-height:1.1}
.brand-square{width:26px;height:26px;background:var(--lime);flex:none}

/* buttons */
.btn{display:inline-flex;align-items:stretch;height:44px;text-decoration:none}
.btn-face{display:flex;align-items:center;gap:8px;padding:0 28px 0 34px;font-weight:800;font-size:13px;text-transform:uppercase;clip-path:polygon(14px 0,100% 0,calc(100% - 14px) 100%,0 100%)}
.btn-slash{width:10px;margin-left:-10px;clip-path:polygon(60% 0,100% 0,40% 100%,0 100%)}
.btn--dark .btn-face{background:var(--ink);color:var(--white)}
.btn--dark .btn-slash{background:var(--lime)}
.btn--lime .btn-face{background:var(--lime);color:var(--ink)}
.btn--lime .btn-slash{background:var(--ink)}
.btn svg{width:13px;height:13px}

/* top bar */
.topbar{left:411px;top:0;width:789px;height:40px;background:var(--lime);clip-path:polygon(0 0,100% 0,100% 100%,22px 100%);display:flex;align-items:center;font-size:14px;font-weight:600}
.topbar-item{position:absolute;display:flex;align-items:center;gap:8px}
.social{position:absolute;left:562px;display:flex;gap:7px}
.social span{width:27px;height:27px;border-radius:50%;background:var(--ink)}

/* nav */
.nav{left:0;top:0;width:1200px;height:0;font-size:14px;font-weight:600;text-transform:uppercase;z-index:2}
.nav a{position:absolute;top:76px;color:var(--ink);text-decoration:none;white-space:nowrap;line-height:18px}
.nav .active{background:var(--lime);padding:2px 8px;border-radius:12px;top:74px}

/* hero */
.hero{left:0;top:133px;width:1200px;height:681px;background:radial-gradient(ellipse at 78% 35%,#d9772a 0%,#8a4220 30%,#3a2418 60%,#191615 100%),#1c1a18}
.hero-title{left:79px;top:305px;font-size:40px;line-height:50px;color:var(--white)}
.hero-title em{font-style:normal;color:var(--lime)}
.hero-sub{left:79px;top:429px;font-size:15px;line-height:29px;font-weight:600;color:var(--white);text-transform:uppercase}

/* about */
.frame-lime{background:var(--lime)}
.photo{background:linear-gradient(135deg,#6b5a3c,#c97a2e 45%,#3d3a33)}
.section-title{font-size:33px;line-height:40px}
.body-text{font-size:13.5px;line-height:26px;color:var(--text);text-align:justify}

/* features */
.features{left:0;top:1456px;width:1200px;height:338px;background:linear-gradient(90deg,#120f0d,#1d1a17 60%,#14110f)}
.feature{position:absolute;top:82px;width:300px;color:var(--white)}
.feature-icon{width:72px;height:72px;border-radius:50%;background:var(--lime);display:flex;align-items:center;justify-content:center}
.feature-icon svg{width:36px;height:36px}
.feature h3{margin-top:38px;font-size:14.5px;font-weight:700;text-transform:uppercase}
.feature p{margin-top:14px;font-size:13.5px;line-height:24px;color:#ddd}

/* offer */
.offer{left:0;top:1794px;width:1200px;height:669px;background:linear-gradient(180deg,#f7f5f2,#f1f1ef 50%,#fbfbfb)}
.offer-list{list-style:none;font-size:14.5px;font-weight:600}
.offer-list li{display:flex;align-items:center;gap:12px;height:32.6px}
.offer-list svg{width:15px;height:15px}

/* projects */
.tabs{left:300px;top:2554px;width:566px;height:57px;display:flex;font-size:14.5px;font-weight:600;text-transform:uppercase}
.tab{display:flex;align-items:center;color:var(--white);background:var(--ink)}
.tab--active{position:relative;width:180px;justify-content:center;background:var(--lime);color:var(--ink)}
.tab--active::after{content:"";position:absolute;left:80px;bottom:-10px;border:10px solid transparent;border-bottom:0;border-top-color:var(--lime)}
.tile{width:314px;height:287px}

/* contact */
.contact-dark{left:0;top:3713px;width:1200px;height:613px;background:linear-gradient(180deg,#171513,#0f0d0c)}
.contact{left:102px;top:3400px;width:995px;height:498px;background:var(--lime)}
.field{position:absolute;background:var(--white);border:1px solid #e1e1e1;padding:12px 20px;font-size:13px;color:#666}
.submit{position:absolute;left:185px;top:369px;width:624px;height:44px;background:var(--ink);color:var(--white);display:flex;align-items:center;justify-content:center;gap:8px;font-size:13px;font-weight:800;text-transform:uppercase}
.submit svg{width:13px;height:13px}

/* footer */
.footer-col{position:absolute;top:4018px;font-size:13.5px;line-height:27.4px;color:var(--white)}
.footer-col h4{font-weight:600;font-size:13.5px;color:var(--lime);margin-bottom:4px}
</style>
</head>
<body>

<!-- header -->
<div class="abs topbar">
  <span class="topbar-item" style="left:47px">
    <svg width="15" height="12" viewBox="0 0 15 12"><rect x="0.5" y="0.5" width="14" height="11" fill="#0d0d0d"/><path d="M1 1l6.5 5L14 1" stroke="#c2d40a" fill="none"/></svg>
    info@gullwindstonecut.example
  </span>
  <span class="topbar-item" style="left:358px">
    <svg width="13" height="13" viewBox="0 0 24 24"><path fill="#0d0d0d" d="M6.6 10.8a15 15 0 006.6 6.6l2.2-2.2a1 1 0 011-.25 11.4 11.4 0 003.6.57 1 1 0 011 1V20a1 1 0 01-1 1A17 17 0 013 4a1 1 0 011-1h3.5a1 1 0 011 1 11.4 11.4 0 00.57 3.6 1 1 0 01-.25 1z"/></svg>
    +61 8 5550 1472
  </span>
  <div class="social"><span></span><span></span><span></span></div>
</div>

<div class="abs brand" style="left:112px;top:50px;width:220px;color:var(--ink)">
  <span class="brand-square"></span><span>Gullwind<br>Stonecut</span>
</div>

<nav class="abs nav">
  <a class="active" style="left:388px">Home</a>
  <a style="left:460px">About Us</a>
  <a style="left:550px">Our Services</a>
  <a style="left:673px">Our Projects</a>
  <a style="left:797px">Contact Us</a>
</nav>

<a class="abs btn btn--dark" style="left:909px;top:65px">
  <span class="btn-face">Get a Quote <svg viewBox="0 0 14 14"><circle cx="7" cy="7" r="7" fill="#fff"/><path d="M5.5 4l3 3-3 3" stroke="#0d0d0d" stroke-width="1.8" fill="none"/></svg></span><span class="btn-slash"></span>
</a>

<!-- hero -->
<div class="abs hero" role="img" aria-label="Yellow excavator on a dirt site under an orange sunset sky"></div>
<h1 class="abs heading hero-title"><em>Raising</em> the standard<br>in earthworks</h1>
<p class="abs hero-sub">Precision excavation and earthmoving services delivering<br>reliable results across Perth and Western Australia.</p>
<a class="abs btn btn--dark" style="left:80px;top:520px">
  <span class="btn-face">Get a Quote <svg viewBox="0 0 14 14"><circle cx="7" cy="7" r="7" fill="#fff"/><path d="M5.5 4l3 3-3 3" stroke="#0d0d0d" stroke-width="1.8" fill="none"/></svg></span><span class="btn-slash"></span>
</a>
<a class="abs btn btn--lime" style="left:270px;top:520px">
  <span class="btn-face">View Projects <svg viewBox="0 0 14 14"><circle cx="7" cy="7" r="7" fill="#0d0d0d"/><path d="M5.5 4l3 3-3 3" stroke="#c2d40a" stroke-width="1.8" fill="none"/></svg></span><span class="btn-slash"></span>
</a>

<!-- about -->
<div class="abs frame-lime" style="left:90px;top:913px;width:355px;height:382px;clip-path:polygon(0 0,100% 0,92% 5%,5% 5%,5% 100%,0 100%)"></div>
<div class="abs photo" style="left:109px;top:931px;width:446px;height:431px" role="img" aria-label="Site worker in hard hat and high-visibility jacket beside an excavator"></div>
<h2 class="abs heading section-title" style="left:624px;top:940px;font-size:30px">About Gullwind Stonecut</h2>
<div class="abs rule" style="left:624px;top:986px"></div>
<div class="abs" style="left:626px;top:1014px;width:474px">
  <p class="body-text">Gullwind Stonecut Earthworks is a Perth-based earthworks and excavation business committed to precision, safety, and dependable delivery. We work closely with builders, developers, and homeowners to ensure every site is prepared to the highest standard — on time and with minimal disruption.</p>
  <p class="body-text" style="margin-top:26px">With modern machinery, skilled operators, and a strong understanding of local conditions, we take pride in providing practical solutions that set a solid foundation for every project.</p>
</div>
<a class="abs btn btn--lime" style="left:628px;top:1280px">
  <span class="btn-face">View More <svg viewBox="0 0 14 14"><circle cx="7" cy="7" r="7" fill="#0d0d0d"/><path d="M5.5 4l3 3-3 3" stroke="#c2d40a" stroke-width="1.8" fill="none"/></svg></span><span class="btn-slash"></span>
</a>

<!-- features -->
<section class="abs features">
  <div class="feature" style="left:110px">
    <div class="feature-icon"><svg viewBox="0 0 24 24" fill="none" stroke="#0d0d0d" stroke-width="1.6"><path d="M12 22s7-7 7-12a7 7 0 10-14 0c0 5 7 12 7 12z"/><circle cx="12" cy="10" r="2.6"/></svg></div>
    <h3>Perth &amp; WA Based</h3>
    <p>Lorem ipsum dolor sit amet, consectetur<br>adipiscing elit, sed do eius</p>
  </div>
  <div class="feature" style="left:471px">
    <div class="feature-icon"><svg viewBox="0 0 24 24" fill="none" stroke="#0d0d0d" stroke-width="1.6"><circle cx="12" cy="12" r="3.2"/><path d="M12 2v3M12 19v3M2 12h3M19 12h3M4.9 4.9l2.1 2.1M17 17l2.1 2.1M4.9 19.1L7 17M17 7l2.1-2.1"/></svg></div>
    <h3>Maintained Equipment</h3>
    <p>Lorem ipsum dolor sit amet, consectetur<br>adipiscing elit, sed do eius</p>
  </div>
  <div class="feature" style="left:832px">
    <div class="feature-icon"><svg viewBox="0 0 24 24" fill="none" stroke="#0d0d0d" stroke-width="1.6"><path d="M12 2l8 3v6c0 5-3.5 9-8 11-4.5-2-8-6-8-11V5z"/><path d="M8.5 12l2.5 2.5 4.5-5"/></svg></div>
    <h3>Safety-Focused</h3>
    <p>Lorem ipsum dolor sit amet, consectetur<br>adipiscing elit, sed do eius</p>
  </div>
</section>

<!-- offer -->
<section class="abs offer"></section>
<h2 class="abs heading section-title" style="left:109px;top:1915px">What We Offer</h2>
<div class="abs rule" style="left:109px;top:1960px"></div>
<p class="abs body-text" style="left:112px;top:1987px;width:450px">We provide a range of professional earthmoving and excavation services tailored to your project requirements.</p>
<ul class="abs offer-list" style="left:112px;top:2056px">
  <li><svg viewBox="0 0 16 16"><circle cx="8" cy="8" r="8" fill="#0d0d0d"/><path d="M4.5 8.2l2.3 2.3 4.7-4.8" stroke="#fff" stroke-width="1.8" fill="none"/></svg>Site cuts &amp; preparation</li>
  <li><svg viewBox="0 0 16 16"><circle cx="8" cy="8" r="8" fill="#0d0d0d"/><path d="M4.5 8.2l2.3 2.3 4.7-4.8" stroke="#fff" stroke-width="1.8" fill="none"/></svg>Trenching &amp; service excavations</li>
  <li><svg viewBox="0 0 16 16"><circle cx="8" cy="8" r="8" fill="#0d0d0d"/><path d="M4.5 8.2l2.3 2.3 4.7-4.8" stroke="#fff" stroke-width="1.8" fill="none"/></svg>Foundations &amp; footings</li>
  <li><svg viewBox="0 0 16 16"><circle cx="8" cy="8" r="8" fill="#0d0d0d"/><path d="M4.5 8.2l2.3 2.3 4.7-4.8" stroke="#fff" stroke-width="1.8" fill="none"/></svg>Land clearing &amp; levelling</li>
  <li><svg viewBox="0 0 16 16"><circle cx="8" cy="8" r="8" fill="#0d0d0d"/><path d="M4.5 8.2l2.3 2.3 4.7-4.8" stroke="#fff" stroke-width="1.8" fill="none"/></svg>Backfilling &amp; compaction</li>
  <li><svg viewBox="0 0 16 16"><circle cx="8" cy="8" r="8" fill="#0d0d0d"/><path d="M4.5 8.2l2.3 2.3 4.7-4.8" stroke="#fff" stroke-width="1.8" fill="none"/></svg>General earthmoving works</li>
</ul>
<a class="abs btn btn--lime" style="left:112px;top:2285px">
  <span class="btn-face">View More <svg viewBox="0 0 14 14"><circle cx="7" cy="7" r="7" fill="#0d0d0d"/><path d="M5.5 4l3 3-3 3" stroke="#c2d40a" stroke-width="1.8" fill="none"/></svg></span><span class="btn-slash"></span>
</a>
<div class="abs frame-lime" style="left:643px;top:1889px;width:354px;height:382px;clip-path:polygon(0 0,100% 0,92% 5%,5% 5%,5% 100%,0 100%)"></div>
<div class="abs" style="left:661px;top:1908px;width:445px;height:428px;background:linear-gradient(180deg,#8b9190,#5a5d55 45%,#6e5238)" role="img" aria-label="Excavator clearing land in a misty pine forest"></div>

<!-- projects -->
<h2 class="abs heading section-title" style="left:0;top:2477px;width:1200px;text-align:center">Recent Projects</h2>
<div class="abs rule" style="left:567px;top:2520px"></div>
<div class="abs tabs">
  <div class="tab tab--active">Residential</div>
  <div class="tab" style="padding-left:36px">Commercial</div>
  <div class="tab" style="padding-left:36px;flex:1">Trenching &amp; Services</div>
</div>
<div class="abs tile" style="left:116px;top:2653px;background:linear-gradient(180deg,#8fb3d6,#b6a78a 45%,#8a5a30)" role="img" aria-label="Excavator digging a trench beside a new house"></div>
<div class="abs tile" style="left:443px;top:2653px;background:linear-gradient(180deg,#c9c4b4,#9c7450 40%,#6b4428)" role="img" aria-label="Pipe laid in an open trench near a house"></div>
<div class="abs tile" style="left:769px;top:2653px;background:linear-gradient(180deg,#d8d3c8,#a8a08e 50%,#7a6f60)" role="img" aria-label="Excavator on a roadworks site with traffic cones"></div>
<div class="abs tile" style="left:116px;top:2955px;background:linear-gradient(180deg,#9ec1e0,#a28a6a 45%,#6e4a2a)" role="img" aria-label="Excavator bucket working near a row of townhouses"></div>
<div class="abs tile" style="left:443px;top:2955px;background:linear-gradient(180deg,#8fa57a,#a48666 50%,#6a4a30)" role="img" aria-label="Large concrete pipe on a residential site"></div>
<div class="abs tile" style="left:769px;top:2955px;background:linear-gradient(180deg,#5f8a3a,#4c6a2a 45%,#3a2618)" role="img" aria-label="Excavator bucket lifting soil on a grassy lot"></div>
<a class="abs btn btn--lime" style="left:510px;top:3276px">
  <span class="btn-face">View More <svg viewBox="0 0 14 14"><circle cx="7" cy="7" r="7" fill="#0d0d0d"/><path d="M5.5 4l3 3-3 3" stroke="#c2d40a" stroke-width="1.8" fill="none"/></svg></span><span class="btn-slash"></span>
</a>

<!-- contact -->
<div class="abs contact-dark" role="img" aria-label="Dark silhouette of earthmoving machinery at dusk"></div>
<section class="abs contact">
  <h2 class="heading section-title" style="position:absolute;left:0;top:77px;width:100%;text-align:center">Connect With Us</h2>
  <p style="position:absolute;left:0;top:144px;width:100%;text-align:center;font-size:15px">Ready to start your project or need expert advice? Contact Gullwind Stonecut Earthworks today.</p>
  <div class="field" style="left:185px;top:204px;width:307px;height:46px">Name</div>
  <div class="field" style="left:185px;top:260px;width:307px;height:44px">Phone</div>
  <div class="field" style="left:185px;top:313px;width:307px;height:46px">Email</div>
  <div class="field" style="left:504px;top:204px;width:305px;height:155px">Message</div>
  <div class="submit">Submit Now <svg viewBox="0 0 14 14"><circle cx="7" cy="7" r="7" fill="#fff"/><path d="M5.5 4l3 3-3 3" stroke="#0d0d0d" stroke-width="1.8" fill="none"/></svg></div>
</section>

<!-- footer -->
<div class="abs brand" style="left:117px;top:4010px;width:230px;color:var(--white)">
  <span class="brand-square"></span><span>Gullwind<br>Stonecut</span>
</div>
<p class="abs" style="left:119px;top:4100px;width:220px;font-size:13.5px;line-height:22px;color:var(--white)">Professional earthworks and excavation services delivering reliable results across Perth and Western Australia.</p>
<div class="footer-col" style="left:445px">
  <h4>Quick Links</h4>Home<br>About<br>Services<br>Projects<br>Contact
</div>
<div class="footer-col" style="left:638px">
  <h4>Services</h4>Site Preparation<br>Excavation<br>Trenching<br>Foundations &amp; Footings<br>Land Clearing<br>General Earthworks
</div>
<div class="footer-col" style="left:869px">
  <h4>Service Areas</h4>Perth Metro<br>Surrounding WA Regions
</div>
<div class="footer-col" style="left:869px;top:4128px;line-height:23.5px">
  <h4>Contact Us</h4>Perth, Western Australia<br>04XX XXX XXX<br>info@gullwindstonecut.example
</div>
<p class="abs" style="left:0;top:4268px;width:1200px;text-align:center;font-size:13px;color:var(--white)">Copyright@2026.All Rights Reserved</p>

</body>
</html>
```